I work in creative/artistic projects across different mediums.
It needs to communicate creativity, style, sexy, uniqueness, individuality and sophistication.
It should not look corporate.
Colours I like are black silver gold deep purple, chocolate, orchid.
It doesn't have to make use of all these colours.
I do not like bright primary colors.
Updates

Project Deadline Extended
Reason: Still in the communication process and to allow the person enough time to finish the design. Though i should know in the next day or two. Thank you.

Target Market(s)

creatives and companies wanting to inject creativity into thier business.

Industry/Entity Type

Work

Contact Information for Business Card

Lionel Crowthwick
0418359026
lionel@lionelcrowthwick.com

quietsilverhour.com.au

Requirements
Should not have
• Anything corporate OR OLD FASHIONED

```html
<!DOCTYPE html>
<html lang="en">
<head>
<meta charset="utf-8">
<title>Lionel Crowthwick — Business Card</title>
<link rel="stylesheet" href="https://fonts.googleapis.com/css2?family=Open+Sans:wght@400&family=Parisienne&display=swap">
<style>
  :root {
    --page: #ece9e4;
    --plum-black: #1b1219;
    --deep-purple: #2e1b2d;
    --dusk-purple: #3d2c3e;
    --haze: #6b6872;
    --khaki: #8f8261;
    --gold: #a28e5f;
    --pale-gold: #b6a57c;
    --name-yellow: #e6e13c;
    --script-yellow: #dcd43f;
    --ink: #2a272c;
  }

  * { margin: 0; padding: 0; box-sizing: border-box; }

  html, body {
    width: 1200px;
    height: 900px;
    overflow: hidden;
    background: var(--page);
  }

  .stage {
    position: relative;
    width: 1200px;
    height: 900px;
  }

  .business-card {
    position: absolute;
    left: 150px;
    top: 175px;
    width: 900px;
    height: 550px;
    background: linear-gradient(
      to bottom,
      var(--plum-black) 0%,
      var(--deep-purple) 22%,
      var(--dusk-purple) 36%,
      var(--haze) 46%,
      var(--khaki) 55%,
      var(--gold) 72%,
      var(--pale-gold) 100%
    );
    box-shadow: 0 10px 30px rgba(0, 0, 0, 0.18);
    font-family: "Open Sans", Arial, sans-serif;
  }

  .card-name {
    position: absolute;
    left: 170px;
    top: 112px;
    font-size: 31px;
    font-weight: 400;
    letter-spacing: 0.62em;
    text-transform: uppercase;
    color: var(--name-yellow);
    white-space: nowrap;
  }

  .card-contact {
    position: absolute;
    left: 0;
    right: 0;
    top: 222px;
    padding-left: 100px;
    text-align: center;
    color: var(--ink);
    font-size: 25px;
    line-height: 1.35;
  }

  .card-contact a {
    color: inherit;
    text-decoration: none;
  }

  .card-website {
    position: absolute;
    left: 34px;
    bottom: 52px;
    font-family: "Parisienne", "Brush Script MT", cursive;
    font-size: 36px;
    color: var(--script-yellow);
    white-space: nowrap;
  }
</style>
</head>
<body>
  <main class="stage">
    <article class="business-card">
      <h1 class="card-name">Lionel Crowthwick</h1>
      <address class="card-contact">
        <a class="contact-email" href="mailto:lionel@lionelcrowthwick.com">lionel@lionelcrowthwick.com</a><br>
        <span class="contact-phone">0418359026</span>
      </address>
      <p class="card-website">quietsilverhour.com.au</p>
    </article>
  </main>
</body>
</html>
```